Christmas Candle Label

We require a Christmas candle label that fits with our current brand (see larkvalewickworks.example, and also example attached). On the attached we would like the word 'Tovane - Mirreld' replaced with 'Merry Christmas' (or something creative that you can come up with) and the writing on the left hand side 'lose yourself in the subtle.........' replaced with 'its beginning to smell a lot like Christmas' (or something creative that you can come up with). We would like the flora image in the background replaced with a line drawing of a Christmas tree or holy or anything else that is appropriate. Finally we are not sure if a different colour label i.e. red, maroon or green (with lots of black, silver or gold writing) instead of black would be best for this label. It may be best to see a comparison of our original black label with black, silver or gold writing, and the other colours.

```html
<!DOCTYPE html>
<html lang="en">
<head>
<meta charset="utf-8">
<title>Larkvale Co. — Christmas Candle Label</title>
<link rel="stylesheet" href="https://fonts.googleapis.com/css2?family=Montserrat:wght@800&family=Yellowtail&family=Old+Standard+TT:wght@400&display=swap">
<style>
  :root {
    --backdrop: #dedede;
    --label-black: #0b0b0b;
    --gold: #d2ad6e;
    --white: #ffffff;
    --snow-band: #d9d9d9;
  }
  html, body {
    margin: 0;
    padding: 0;
    width: 1135px;
    height: 1200px;
    overflow: hidden;
    background: var(--backdrop);
  }
  .label {
    position: absolute;
    left: 40px;
    top: 373px;
    width: 1055px;
    height: 453px;
    background: var(--label-black);
    color: var(--white);
    font-family: "Old Standard TT", Georgia, serif;
  }
  .batch {
    position: absolute;
    left: 892px;
    top: 48px;
    font-size: 14px;
    word-spacing: 22px;
  }
  .brand-name {
    position: absolute;
    left: 0;
    width: 100%;
    top: 76px;
    text-align: center;
    color: var(--gold);
    font-size: 20px;
    letter-spacing: 1px;
  }
  .title {
    position: absolute;
    left: 0;
    width: 100%;
    text-align: center;
    margin: 0;
  }
  .title-merry {
    top: 152px;
    font-family: "Montserrat", Arial, sans-serif;
    font-weight: 800;
    font-size: 40px;
    line-height: 44px;
  }
  .title-christmas {
    top: 180px;
    font-family: "Yellowtail", cursive;
    font-weight: 400;
    font-size: 92px;
    line-height: 100px;
    color: var(--gold);
  }
  .tagline {
    position: absolute;
    left: 0;
    width: 100%;
    top: 307px;
    text-align: center;
    font-size: 11px;
    letter-spacing: 2px;
  }
  .origin {
    position: absolute;
    left: 0;
    width: 100%;
    top: 331px;
    text-align: center;
    font-size: 14px;
    line-height: 14px;
  }
  .slogan {
    position: absolute;
    left: 27px;
    top: 246px;
    font-size: 24px;
    line-height: 30px;
    margin: 0;
  }
  .slogan .highlight { color: var(--gold); }
  .product-info {
    position: absolute;
    right: 27px;
    top: 190px;
    text-align: right;
    font-size: 14px;
    line-height: 19px;
  }
  .product-info p { margin: 0 0 11px; }
  .product-info .natural { color: var(--gold); }
  .snowflake-border {
    position: absolute;
    left: 14px;
    right: 14px;
    top: 390px;
    height: 54px;
    background: linear-gradient(90deg, #cfcfcf, #f2f2f2 50%, #cfcfcf);
    opacity: 0.85;
  }
</style>
</head>
<body>
  <section class="label">
    <div class="batch">Batch: / /</div>
    <div class="brand-name">Larkvale Co.</div>

    <h1 class="title title-merry">MERRY</h1>
    <h2 class="title title-christmas">Christmas</h2>

    <div class="tagline">UNTAMED TASMANIAN WILDERNESS</div>
    <div class="origin">Handcrafted in<br>SOUTHERN TASMANIA</div>

    <p class="slogan">its beginning<br>to smell a<br>lot like<br><span class="highlight">Christmas</span></p>

    <div class="product-info">
      <p>500g<br>90+ Hours</p>
      <p>Hand poured,<br>scented soy and<br>coconut candle</p>
      <p class="natural">Made with all<br>natural ingredients</p>
    </div>

    <div class="snowflake-border" role="img" aria-label="Decorative border of white snowflakes along the bottom edge"></div>
  </section>
</body>
</html>
```